Corvale Homes

To produce a business card design for our newly established house building and development company, We have had a logo design done please see attached, our slogan is "building your home sweet home"
Contact Information for Business Card
Adress on card needs to Read - 58 Elmsworth Lane, Harrowdale, Westmarsh HD7 4QT. Director name Dean Vascotti
Requirements
Must have
- Web adress is www.corvale-homes.co.uk
- Email address is info@corvale-homes.co.uk
- phone number 07700 900417

```html
<!DOCTYPE html>
<html lang="en">
<head>
<meta charset="utf-8">
<title>Corvale Homes – Business Card</title>
<link href="https://fonts.googleapis.com/css2?family=Arimo:wght@400;700&display=swap" rel="stylesheet">
<style>
  :root {
    --green: #8cc243;
    --grey: #8a8a8a;
    --text-grey: #707070;
    --white: #ffffff;
    --backdrop: #3a3a3a;
  }
  * { margin: 0; padding: 0; box-sizing: border-box; }
  html, body {
    width: 1200px; height: 1200px; overflow: hidden;
    background: var(--backdrop);
    font-family: "Arimo", Arial, sans-serif;
  }
  .canvas { position: relative; width: 1200px; height: 1200px; }

  .card { position: absolute; background: var(--white); overflow: hidden; }
  .card--front { left: 313px; top: 247px; width: 574px; height: 319px; }
  .card--back  { left: 313px; top: 634px; width: 576px; height: 319px; }

  .front-band {
    position: absolute; left: 190px; width: 193px; height: 45px;
    background: var(--green);
  }
  .front-band--top { top: 0; }
  .front-band--bottom { bottom: 0; }

  .brand-name {
    position: absolute;
    font-weight: 700;
    color: var(--green);
    white-space: nowrap;
    transform: translate(-50%, -50%);
  }
  .card--front .brand-name { left: 287px; top: 160px; font-size: 38px; }
  .card--back .brand-name { left: 125px; top: 222px; font-size: 26px; }

  .holder { position: absolute; left: 31px; top: 28px; }
  .holder-name { font-size: 23px; font-weight: 700; color: var(--grey); line-height: 1.2; }
  .holder-role { font-size: 21px; color: var(--green); line-height: 1.2; margin-top: 6px; }

  .contact {
    position: absolute; right: 105px;
    font-size: 17px; color: var(--text-grey);
    text-align: right; line-height: 22px;
    transform: translateY(-50%);
    white-space: nowrap;
  }
  .contact--phone { top: 124px; font-size: 19px; }
  .contact--email { top: 171px; }
  .contact--web   { top: 217px; }
  .contact--address { top: 271px; font-size: 17.5px; }

  .icon-strip {
    position: absolute; right: 0; top: 0; width: 89px; height: 100%;
    background: var(--green);
  }
  .icon-row { position: absolute; left: 0; width: 89px; height: 40px; transform: translateY(-50%); }
  .icon-row::after {
    content: ""; position: absolute; left: 44px; right: 0; top: 50%;
    height: 20px; transform: translateY(-50%); background: var(--white);
  }
  .icon-row svg { position: absolute; left: 11px; top: 1px; width: 38px; height: 38px; z-index: 1; }
</style>
</head>
<body>
<main class="canvas">

  <section class="card card--front" aria-label="Business card front">
    <div class="front-band front-band--top"></div>
    <span class="brand-name">Corvale Homes</span>
    <div class="front-band front-band--bottom"></div>
  </section>

  <section class="card card--back" aria-label="Business card back">
    <div class="holder">
      <p class="holder-name">Dean Vascotti</p>
      <p class="holder-role">Director</p>
    </div>

    <span class="brand-name">Corvale Homes</span>

    <p class="contact contact--phone">07700 900417</p>
    <p class="contact contact--email">info@corvale-homes.co.uk</p>
    <p class="contact contact--web">www.corvale-homes.co.uk</p>
    <p class="contact contact--address">58 Elmsworth Lane, Harrowdale,<br>Westmarsh HD7 4QT.</p>

    <div class="icon-strip">
      <div class="icon-row" style="top:125px">
        <svg viewBox="0 0 38 38"><circle cx="19" cy="19" r="17" fill="var(--green)" stroke="#fff" stroke-width="2.5"/>
          <path d="M13 10c1-1 2.5-1 3 0l2 4c.4.8 0 1.6-.6 2.1l-1.2 1c.9 2 2.5 3.7 4.5 4.6l1-1.2c.6-.6 1.4-.9 2.1-.5l4 2c1 .5 1 2 0 3l-1.5 1.5c-1.5 1.5-4 1.3-7-.6-3-2-5.6-4.7-7.3-7.6-1.6-2.8-1.6-5.3-.2-6.8z" fill="#fff"/></svg>
      </div>
      <div class="icon-row" style="top:171px">
        <svg viewBox="0 0 38 38"><circle cx="19" cy="19" r="17" fill="var(--green)" stroke="#fff" stroke-width="2.5"/>
          <rect x="10" y="13" width="18" height="12" fill="#fff"/>
          <path d="M10 13l9 7 9-7M10 25l7-6M28 25l-7-6" fill="none" stroke="var(--green)" stroke-width="1.3"/></svg>
      </div>
      <div class="icon-row" style="top:216px">
        <svg viewBox="0 0 38 38"><circle cx="19" cy="19" r="17" fill="var(--green)" stroke="#fff" stroke-width="2.5"/>
          <circle cx="19" cy="19" r="10" fill="#fff"/>
          <path d="M19 9c-3 3-3 17 0 20M19 9c3 3 3 17 0 20M9 19h20M11 14h16M11 24h16" fill="none" stroke="var(--green)" stroke-width="1.2"/></svg>
      </div>
      <div class="icon-row" style="top:262px">
        <svg viewBox="0 0 38 38"><circle cx="19" cy="19" r="17" fill="var(--green)" stroke="#fff" stroke-width="2.5"/>
          <path d="M19 9l11 10h-3v9h-5v-6h-6v6h-5v-9H8z" fill="#fff"/></svg>
      </div>
    </div>
  </section>

</main>
</body>
</html>
```